Business Card & Logo Design Project

I am looking for a slick/simple design for a logo and business card, for a music Producer/Mixer/Engineer.

I'm based in Tokyo, Japan and I help my clients polish up their creation to major radio/TV status. My clients pay me for my taste, sense of balance expertise and creative direction/

Design should give impression of seal of quality, professionalism, and enthusiasm need some sort of a logo like design for "vantrix productions".

Please don't include music notes or instruments or anything musically related and anything samurai or ninja or too much Japan in them on the design.

I like clever, slick stuff that's not too obvious.
I also like a smooth gradation type transition. My favorite color is deep dark blue/

Good Luck and Thank you for your effort.
Updates

I would like a two-sided design for this one.
One side with "vantrix productions" (all lower case) on, and the other side with my name and contact info.

Please also consider portrait position (or direction).  (as opposed to landscape) 

Target Market(s)

My primary targets are artists & bands, who want absolute best for their creation.

Industry/Entity Type

Business

Requirements
Must have
• Two-Sided
1, vantrix productions
2, Kenji Harumoto, Producer/Mixer/Engineer, +81 090 4827 3516, brambleway@mailnest.example
Nice to have
• Any suggestions are welcome//
Should not have
• Anything music related images.
(e.g. CD, music notations, instruments etc.)

```html
<!DOCTYPE html>
<html lang="en">
<head>
<meta charset="utf-8">
<title>vantrix productions — business cards</title>
<link rel="stylesheet" href="https://fonts.googleapis.com/css2?family=Bodoni+Moda:wght@400;500&display=swap">
<style>
  :root {
    --paper: #ffffff;
    --paper-soft: #f7f9fb;
    --ink: #111111;
    --frame: #3a1a1a;
    --blue-deep: #2a4bff;
    --blue-mid: #1f8cff;
    --cyan: #00f4ff;
    --ink-blue: #2233ee;
    --orange: #ff9a00;
    --orange-pale: #fbe7cc;
    --band-black: #111111;
    --divider: #e0335a;
  }
  * { box-sizing: border-box; margin: 0; padding: 0; }
  html, body {
    width: 1200px; height: 918px; overflow: hidden;
    background: var(--paper);
    font-family: "Bodoni Moda", "Times New Roman", serif;
  }
  .sheet { position: relative; width: 1200px; height: 918px; }

  .card { position: absolute; overflow: hidden; }

  /* Blue series */
  .card--blue {
    width: 546px; height: 347px; top: 0;
    background: var(--paper);
    border: 1px solid var(--ink);
  }
  .card--blue.front { left: 11px; }
  .card--blue.back { left: 654px; }
  .blue-band {
    position: absolute; left: 0; right: 0; top: 59px; height: 228px;
    background: linear-gradient(90deg, var(--blue-deep) 0%, var(--blue-mid) 22%, var(--cyan) 48%, var(--blue-mid) 78%, var(--blue-deep) 100%);
  }
  .front .mark-dot {
    position: absolute; left: 30px; top: 92px;
    width: 130px; height: 130px; border-radius: 50%;
    background: var(--ink);
  }
  .front .studio-name {
    position: absolute; right: 18px; top: 222px;
    font-size: 36px; font-weight: 500; color: var(--ink);
  }
  .back .contact {
    position: absolute; left: 0; right: 0; top: 62px;
    text-align: center; color: var(--ink);
  }
  .contact .person { font-size: 39px; line-height: 1.1; }
  .contact .roles { font-size: 25px; line-height: 1.2; }
  .contact .phone { font-size: 24px; margin-top: 28px; }
  .contact .email { font-size: 24px; margin-top: 26px; }
  .back .footer-name {
    position: absolute; right: 20px; top: 298px;
    font-size: 19px; font-weight: 500; color: var(--ink);
  }

  /* Orange series */
  .card--orange {
    width: 545px; height: 347px; top: 570px;
    background: var(--paper-soft);
    border: 2px solid var(--frame);
    border-radius: 24px;
  }
  .card--orange.front { left: 0; }
  .card--orange.back { left: 567px; }
  .orange-band {
    position: absolute; left: 0; right: 0; top: 243px; height: 49px;
  }
  .front .orange-band {
    background: linear-gradient(90deg, var(--band-black) 0%, var(--orange) 32%, var(--orange-pale) 70%, var(--paper-soft) 100%);
  }
  .back .orange-band {
    background: linear-gradient(90deg, var(--paper-soft) 0%, var(--orange-pale) 18%, var(--orange) 58%, var(--band-black) 92%);
  }
  .card--orange .mark-dot {
    position: absolute; border-radius: 50%;
  }
  .front .mark-dot--blue {
    left: 26px; top: 20px; width: 68px; height: 68px;
    background: var(--ink-blue);
  }
  .back .mark-dot--black {
    right: 24px; top: 20px; width: 44px; height: 44px;
    background: var(--ink);
  }
  .band-name {
    position: absolute; right: 12px; top: 251px;
    font-size: 27px; font-weight: 500;
  }
  .front .band-name { color: var(--ink-blue); }
  .back .band-name { color: var(--paper); font-size: 22px; top: 256px; }
  .back .contact-left {
    position: absolute; left: 20px; top: 14px; color: var(--ink-blue);
  }
  .contact-left .person { font-size: 35px; line-height: 1.1; }
  .contact-left .roles { font-size: 24px; line-height: 1.25; }
  .contact-left .roles .sep { color: var(--divider); }
  .contact-left .phone { font-size: 24px; margin-top: 26px; }
  .contact-left .email { font-size: 23px; margin-top: 24px; }
</style>
</head>
<body>
<main class="sheet">

  <section class="card card--blue front">
    <div class="blue-band"></div>
    <div class="mark-dot"></div>
    <div class="studio-name">vantrix productions</div>
  </section>

  <section class="card card--blue back">
    <div class="blue-band"></div>
    <div class="contact">
      <p class="person">Kenji Harumoto</p>
      <p class="roles">Producer | Mixer | Engineer</p>
      <p class="phone">(+81) 090 4827 3516</p>
      <p class="email">brambleway@mailnest.example</p>
    </div>
    <div class="footer-name">vantrix productions</div>
  </section>

  <section class="card card--orange front">
    <div class="mark-dot mark-dot--blue"></div>
    <div class="orange-band"></div>
    <div class="band-name">vantrix productions</div>
  </section>

  <section class="card card--orange back">
    <div class="contact-left">
      <p class="person">Kenji Harumoto</p>
      <p class="roles">Producer <span class="sep">|</span> Mixer <span class="sep">|</span> Engineer</p>
      <p class="phone">(+81) 090 4827 3516</p>
      <p class="email">brambleway@mailnest.example</p>
    </div>
    <div class="mark-dot mark-dot--black"></div>
    <div class="orange-band"></div>
    <div class="band-name">vantrix productions</div>
  </section>

</main>
</body>
</html>
```